Corporate-Design für Handwerks- und Dienstleistungsfirma
Erster Vorschlag Logo hat mich nicht mehr losgelassen. Meine Wünsche wurden sehr schnell erfasst und umgesetzt, Top Service Besten Dank!
Zielgruppe
Ich gründe eine Einzelfirma und biete Dienstleistungen im Bereich Handwerk jeglicher Art, mit Schwerpunkt Holz. Zielgruppe Privatpersonen, Verwaltungen etc.
Aufgabenstellung
Den Namen Handwerk und Dienstleistung sollen im Vordergrund stehen, Name, Telefon, E Mail eher Zweitrangig, muss aber bei einem Einzelunternehmen aufgeführt werden.

```html
<!DOCTYPE html>
<html lang="de">
<head>
<meta charset="utf-8">
<title>Hubert Melk – Corporate Design</title>
<link href="https://fonts.googleapis.com/css2?family=Ubuntu:wght@400;700&family=Oswald:wght@400&family=Bree+Serif&display=swap" rel="stylesheet">
<style>
  :root{
    --paper:#f7f7f7;
    --green:#93c01f;
    --ink:#4a494d;
    --text:#1d1d1f;
    --white:#ffffff;
    --sign:#1f5fb0;
  }
  *{margin:0;padding:0;box-sizing:border-box}
  html,body{width:1200px;height:2402px;overflow:hidden}
  body{position:relative;background:var(--green);font-family:"Ubuntu",sans-serif;color:var(--text)}
  .stage-top{position:absolute;left:0;top:0;width:1200px;height:670px;background:var(--paper)}
  .brand{position:absolute;display:flex;align-items:center;justify-content:center;gap:.5em;
    font-family:"Ubuntu",sans-serif;font-weight:700;color:var(--ink);white-space:nowrap}
  .brand .dot{display:block;border-radius:50%;background:var(--ink)}
  .brand-hero{left:0;top:300px;width:1200px;font-size:72px}
  .brand-hero .dot{width:56px;height:56px}
  .card{position:absolute;top:738px;width:372px;height:240px;box-shadow:18px 22px 26px rgba(40,60,0,.35)}
  .card-front{left:196px;background:var(--white)}
  .card-front .brand{left:0;top:100px;width:372px;font-size:32px}
  .card-front .dot{width:26px;height:26px}
  .card-back{left:634px;background:var(--ink);color:var(--white)}
  .contact{position:absolute;font-family:"Oswald",sans-serif;color:var(--white);line-height:1}
  .contact .phone{display:block;font-size:30px;letter-spacing:-1px}
  .contact .mail{display:block;font-size:14px;margin-top:6px}
  .card-back .contact{left:106px;top:102px}
  .letter{position:absolute;left:142px;top:1033px;width:920px;height:1299px;background:var(--white);
    box-shadow:-20px 24px 30px rgba(40,60,0,.35)}
  .letter .brand{left:610px;top:108px;width:260px;font-size:30px}
  .letter .dot{width:24px;height:24px}
  .letter-band{position:absolute;left:648px;top:237px;width:272px;height:88px;background:var(--ink)}
  .letter-band .contact{left:24px;top:20px}
  .letter-band .phone{font-size:29px}
  .sender{position:absolute;left:95px;top:191px;width:392px;padding-bottom:3px;border-bottom:1.5px solid var(--ink);
    font-family:"Bree Serif",serif;font-size:13.5px;color:var(--ink);text-align:center}
  .recipient{position:absolute;left:115px;top:236px;font-size:20px;line-height:28.5px;letter-spacing:.3px}
  .recipient .zip{margin-top:28px}
  .body{position:absolute;left:115px;top:516px;width:690px;font-size:20px;line-height:28.3px;letter-spacing:.3px}
  .body p{margin-bottom:10px}
  .body .salute{margin-bottom:28px}
  .body .close{margin-top:26px}
  .signature{position:absolute;left:115px;top:1150px;width:300px;height:46px;
    background:linear-gradient(90deg,rgba(31,95,176,.22),rgba(31,95,176,.06))}
</style>
</head>
<body>
  <section class="stage-top">
    <div class="brand brand-hero"><span class="dot"></span>Hubert Melk</div>
  </section>

  <div class="card card-front">
    <div class="brand"><span class="dot"></span>Hubert Melk</div>
  </div>
  <div class="card card-back">
    <div class="contact"><span class="phone">+41 79 555 01 28</span><span class="mail">melk.hubert@werkpost.example</span></div>
  </div>

  <article class="letter">
    <div class="brand"><span class="dot"></span>Hubert Melk</div>
    <div class="letter-band">
      <div class="contact"><span class="phone">+41 79 555 01 28</span><span class="mail">melk.hubert@werkpost.example</span></div>
    </div>
    <div class="sender">Hubert Melk | Beispielstrassse 123 | 54321 Musterstadt</div>
    <div class="recipient">
      Lorem ipsum dolor<br>consectetuer adipiscing elit<br>autem vel eum 123
      <div class="zip">54321 consequat</div>
    </div>
    <div class="body">
      <p class="salute">Lorem ipsum dolor sit,</p>
      <p>amet, consectetuer adipiscing elit, sed diam nonummy nibh euismod tincidunt ut laoreet dolore magna aliquam erat volut­pat. Ut wisi enim ad minim veniam, quis nostrud exerci tation ullamcorper suscipit lobortis nisl ut aliquip ex ea commodo consequat.</p>
      <p>Duis autem vel eum iriure dolor in hendrerit in vulputate velit esse molestie consequat, vel illum dolore eu feugiat nulla facili­sis at vero eros et accumsan et iusto odio dignissim qui blandit nulla facilisi.</p>
      <p>Lorem ipsum dolor sit amet, cons ectetuer adipiscing elit, sed diam nonummy nibh euismod tincidunt ut laoreet dolore magna nostrud exerci tation ullamcorper suscipit lobortis nisl ut aliquip ex ea commodo consequat.</p>
      <p>Dolor sit amet, consectetuer adipiscing elit, sed diam nonummy nibh euismod tincidunt ut laoreet dolore magna nostrud exerci tation ullamcorper suscipit lobortis nisl ut aliquip ex ea commo­do consequat.</p>
      <p class="close">Duis autem vel eum</p>
    </div>
    <div class="signature" role="img" aria-label="Handschriftliche Unterschrift in Blau"></div>
  </article>
</body>
</html>
```